Scientific Web Site for TRELDMIST

Professional Scientific / Service orientated web site, motto, new logos attached for viewing.

"We measure so the Business Owner can Manage" their environments.
Site needs to be be mobile friendly.

We provide a service to electronically measure cleanliness of any surface and a value added disinfecting fogging surface.

Reports showing locations, trending, tracking and randomized test plans ongoing audits will be made available..

NOTE: Although image of Corona Virus is current we don't wont it plastered through the web site, their is more than the current virus.

Home Page - Professional Scientific / Service Looking
About
Our Approach
Services
Residential
Commercial
Transportation
Gyms
Educational & Daycare
Real Estate - Open for inspections, End of Lease etc

Contact
Mobile #
Email
Form to leave their details

Links to social media, Facebook, Instagram
Reference Sites: Ranked in preference
www.orlimber.com.au
https://www.brightquarrymethods.co.uk/
https://www.vantopel.com/
https://www.kwtpure.com.au/specialist-surface-disinfection/
https://www.artmosaicly.com/design/48102957
https://www.artmosaicly.com/design/48736614
https://www.artmosaicly.com/design/48029561

Target Market(s)

Commercial and professional Services

Font styles to use
Sans Serif

Requirements
Must have
• Wix Website
Clean fresh look with appropriate imaging
Web site is a company advertising that will hold static information and we will market through social media.
Nice to have
• Scientific look and feel
Should not have
• Prominent Corona Virus images or references

```html
<!DOCTYPE html>
<html lang="en">
<head>
<meta charset="utf-8">
<title>TRELDMIST – Electronically Measure Cleanliness</title>
<link rel="stylesheet" href="https://fonts.googleapis.com/css2?family=Poppins:ital,wght@0,400;0,500;0,600;0,700;0,800;0,900;1,400&display=swap">
<style>
:root{
  --orange:#f5821f;
  --orange-deep:#e86d0c;
  --ink:#222222;
  --grey-text:#777777;
  --slate:#4a4a4d;
  --footer:#231f20;
  --footer-deep:#1b1819;
  --line:#d8d8d8;
  --white:#ffffff;
}
*{margin:0;padding:0;box-sizing:border-box}
html,body{width:1200px;height:4187px;overflow:hidden}
body{font-family:'Poppins',sans-serif;color:var(--ink);background:var(--white);position:relative}
.abs{position:absolute}
.section-title{position:absolute;left:0;width:1200px;text-align:center;color:var(--orange);font-weight:700;font-size:33px;letter-spacing:.5px}
.section-lead{position:absolute;left:250px;width:700px;text-align:center;font-size:12.5px;line-height:23px;color:var(--grey-text)}

/* header */
.site-header{position:absolute;top:0;left:0;width:1200px;height:125px;background:var(--white)}
.brand{position:absolute;left:126px;top:58px;font-weight:600;font-size:22px;letter-spacing:3px;color:var(--ink);display:flex;align-items:center;gap:10px}
.brand-dot{width:10px;height:10px;border-radius:50%;background:var(--orange)}
.main-nav{position:absolute;left:468px;top:64px;display:flex;gap:22px;font-size:13.5px;color:#333}
.main-nav .active{color:var(--orange)}
.header-phone{position:absolute;left:955px;top:63px;font-size:13.5px;font-weight:600;display:flex;align-items:center;gap:10px}

/* hero */
.hero{position:absolute;top:125px;left:0;width:1200px;height:547px;background:linear-gradient(100deg,#7a3a0c 0%,#c7600f 35%,#f08a24 60%,#e0781a 100%)}
.hero-title{position:absolute;left:127px;top:98px;font-weight:800;font-size:55px;line-height:62px;color:var(--white);letter-spacing:-1px}
.hero-text{position:absolute;left:129px;top:310px;width:380px;font-size:17px;line-height:27px;color:var(--white)}
.hero-dots{position:absolute;left:125px;top:424px;display:flex;gap:20px;align-items:center}
.hero-dots span{width:7px;height:7px;border-radius:50%;background:var(--white)}
.hero-dots .current{width:13px;height:13px;background:transparent;border:2px solid var(--white);position:relative}
.hero-dots .current::after{content:"";position:absolute;left:2px;top:2px;width:5px;height:5px;border-radius:50%;background:var(--white)}

/* about */
.btn{position:absolute;background:var(--orange);color:var(--white);border-radius:22px;text-align:center;font-size:12px;font-weight:500}

/* approach */
.approach{position:absolute;top:1070px;left:0;width:1200px;height:517px}
.approach-copy{position:absolute;left:0;top:0;width:599px;height:517px;background:linear-gradient(180deg,#58585b 0%,#464649 60%,#3a3a3d 100%)}
.approach-photo{position:absolute;left:599px;top:0;width:601px;height:517px;background:linear-gradient(120deg,#f79a3c 0%,#ee7f1c 50%,#f08a2a 100%)}
.approach h2{position:absolute;left:130px;top:154px;font-size:33px;font-weight:700;color:var(--white)}
.approach p{position:absolute;left:132px;color:var(--white);font-size:12.5px;line-height:23px}
.approach .note{font-style:italic}

/* services */
.service{position:absolute;width:300px}
.service h3{font-size:18px;font-weight:600;color:#444}
.service p{font-size:12.5px;line-height:22.5px;color:var(--grey-text);margin-top:20px}
.service.left{text-align:right}
.service-icon{position:absolute;width:74px;height:74px}

/* areas */
.areas{position:absolute;top:2325px;left:0;width:1200px;height:648px;background:linear-gradient(90deg,#ec7a1b 0%,#f58a2a 45%,#ef7d1e 100%)}
.areas .section-title{color:var(--white);top:78px}
.area-card{position:absolute;top:190px;width:276px;height:360px;background:var(--white)}
.area-photo{height:192px}
.area-card h3{position:absolute;left:38px;top:227px;color:var(--orange);font-size:18px;font-weight:600}
.area-card p{position:absolute;left:38px;top:272px;width:210px;font-size:12.5px;line-height:22.5px;color:var(--grey-text)}

/* contact */
.field{position:absolute;height:41px;border:1px solid var(--line);border-radius:21px;padding-left:20px;font-size:12.5px;color:#666;line-height:39px}
.field.message{height:96px;border-radius:48px;line-height:94px}

/* footer */
.site-footer{position:absolute;top:3675px;left:0;width:1200px;height:512px;background:var(--footer);color:#cfcfcf}
.footer-bar{position:absolute;left:0;top:422px;width:1200px;height:90px;background:var(--footer-deep)}
.footer-bar p{text-align:center;font-size:10px;color:#6a6a6a;margin-top:37px}
.footer-col h4{position:absolute;top:90px;font-size:16px;font-weight:600;color:var(--white)}
.footer-list{position:absolute;list-style:none;font-size:12.5px}
.footer-list li{height:29px;display:flex;align-items:center;gap:16px}
.footer-list li::before{content:"";width:10px;height:8px;flex:none;background:linear-gradient(var(--white),var(--white)) left center/8px 1.5px no-repeat;clip-path:polygon(0 42%,60% 42%,60% 0,100% 50%,60% 100%,60% 58%,0 58%)}
.contact-row{position:absolute;left:161px;display:flex;gap:34px;font-size:12.5px;line-height:18px}
.footer-brand{position:absolute;left:904px;top:164px;font-weight:600;font-size:25px;letter-spacing:3px;color:var(--white)}
.social{position:absolute;top:228px;width:30px;height:30px;border-radius:50%;background:var(--white)}
</style>
</head>
<body>

<header class="site-header">
  <div class="brand"><span>TRELDMIST</span><span class="brand-dot"></span></div>
  <nav class="main-nav">
    <span class="active">Home</span><span>About</span><span>Our Approach</span><span>Our Services</span><span>Contact</span>
  </nav>
  <div class="header-phone">
    <svg width="18" height="18" viewBox="0 0 24 24" fill="none" stroke="#222" stroke-width="1.8"><path d="M5 3h4l2 5-2.5 1.5a11 11 0 0 0 6 6L16 13l5 2v4a2 2 0 0 1-2 2A16 16 0 0 1 3 5a2 2 0 0 1 2-2z"/></svg>
    <span>123-456-7890</span>
  </div>
</header>

<section class="hero" role="img" aria-label="Orange-toned microscopic scene with a DNA strand and a cell">
  <h1 class="hero-title">Electronically<br>Measure<br>Cleanliness</h1>
  <p class="hero-text">We provide a service to electronically measure cleanliness of any surface and a value added disinfecting fogging surface.</p>
  <div class="hero-dots"><span class="current"></span><span></span><span></span></div>
</section>

<section class="about">
  <h2 class="section-title" style="top:772px">ABOUT COMPANY</h2>
  <p class="section-lead" style="top:843px;left:240px;width:720px">Sed ut perspiciatis unde omnis iste natus error sit voluptatem accusantium doloremque laudantium.Sed ut perspiciatis unde omnis iste natus error sit voluptatem accusantium doloremque laudantium.Sed ut perspiciatis unde omnis iste natus error sit voluptatem accusantium doloremque ium.doloremque</p>
  <div class="btn" style="left:536px;top:943px;width:130px;height:40px;line-height:40px">View More</div>
</section>

<section class="approach">
  <div class="approach-copy" role="img" aria-label="Dark grey laboratory glassware background">
    <h2>OUR APPROACH</h2>
    <p style="top:215px;width:400px">Sed ut perspiciatis unde omnis iste natus error sit voluptatem accusantium doloremque laudantium.</p>
    <p class="note" style="top:295px;width:260px">Locations, Trending, Tracking and Randomized test plans ongoing audits will be made available..</p>
  </div>
  <div class="approach-photo" role="img" aria-label="Scientist looking through a microscope, orange tinted"></div>
</section>

<section class="services">
  <h2 class="section-title" style="top:1680px">OUR SERVICES</h2>
  <p class="section-lead" style="top:1751px">Sed ut perspiciatis unde omnis iste natus error sit voluptatem accusantium doloremque laudantium.Sed ut perspiciatis unde omnis iste natus error sit voluptatem accusantium doloremque laudant</p>

  <svg class="abs" style="left:410px;top:1838px" width="380" height="380" viewBox="0 0 380 380">
    <circle cx="190" cy="190" r="175" fill="none" stroke="#999" stroke-width="1.3" stroke-dasharray="5 6"/>
    <circle cx="190" cy="190" r="145" fill="#f3f3f3" stroke="#f5821f" stroke-width="4"/>
    <circle cx="52" cy="80" r="7" fill="#f5821f"/>
    <circle cx="326" cy="78" r="7" fill="#f5821f"/>
    <circle cx="32" cy="260" r="7" fill="#f5821f"/>
    <circle cx="343" cy="270" r="7" fill="#f5821f"/>
    <text x="190" y="199" text-anchor="middle" font-family="Poppins, sans-serif" font-weight="600" font-size="26" letter-spacing="3" fill="#222">TRELDMIST</text>
  </svg>

  <svg class="service-icon" style="left:326px;top:1859px" viewBox="0 0 74 74" fill="none" stroke="#f5821f" stroke-width="2">
    <circle cx="37" cy="37" r="35"/><path d="M20 38l17-14 17 14M25 34v16h24V34"/>
  </svg>
  <div class="service left" style="left:82px;top:1903px">
    <h3 style="margin-right:90px">Residential</h3>
    <p>Sed ut perspiciatis unde omnis iste natus error sit voluptatem accusantium dolorem-que laudantium.</p>
  </div>
  <svg class="service-icon" style="left:326px;top:2061px" viewBox="0 0 74 74" fill="none" stroke="#f5821f" stroke-width="2">
    <circle cx="37" cy="37" r="35"/><rect x="22" y="24" width="30" height="22" rx="3"/><circle cx="28" cy="50" r="3"/><circle cx="46" cy="50" r="3"/>
  </svg>
  <div class="service left" style="left:82px;top:2103px">
    <h3 style="margin-right:90px">Transportation</h3>
    <p>Sed ut perspiciatis unde omnis iste natus error sit voluptatem accusantium dolorem-que laudantium.</p>
  </div>
  <svg class="service-icon" style="left:805px;top:1859px" viewBox="0 0 74 74" fill="none" stroke="#f5821f" stroke-width="2">
    <circle cx="37" cy="37" r="35"/><rect x="26" y="20" width="22" height="34"/><path d="M31 27h4M39 27h4M31 34h4M39 34h4M31 41h4M39 41h4"/>
  </svg>
  <div class="service" style="left:813px;top:1903px">
    <h3 style="margin-left:86px">Commercial</h3>
    <p>Sed ut perspiciatis unde omnis iste natus error sit voluptatem accusantium dolorem-que laudantium.</p>
  </div>
  <svg class="service-icon" style="left:805px;top:2061px" viewBox="0 0 74 74" fill="none" stroke="#f5821f" stroke-width="2">
    <circle cx="37" cy="37" r="35"/><path d="M24 37h26M22 29v16M27 31v12M52 29v16M47 31v12"/>
  </svg>
  <div class="service" style="left:813px;top:2103px">
    <h3 style="margin-left:86px">Gyms</h3>
    <p>Sed ut perspiciatis unde omnis iste natus error sit voluptatem accusantium dolorem-que laudantium.</p>
  </div>
</section>

<section class="areas" role="img" aria-label="Orange background with a connected network of nodes over a keyboard">
  <h2 class="section-title">AREAS WE SERVE</h2>
  <div class="area-card" style="left:148px">
    <div class="area-photo" role="img" aria-label="Hand touching a digital touchscreen" style="background:linear-gradient(135deg,#cfe0f2,#5d86b8 60%,#2c4f83)"></div>
    <h3>Commercial</h3>
    <p>Sed ut perspiciatis unde omnis iste natus error sit</p>
  </div>
  <div class="area-card" style="left:469px">
    <div class="area-photo" role="img" aria-label="Person in yellow gloves wiping a table at home" style="background:linear-gradient(135deg,#eef2e4,#c9d8a8 45%,#d9b86a 75%,#a2779a)"></div>
    <h3>Residential</h3>
    <p>Sed ut perspiciatis unde omnis iste natus error sit</p>
  </div>
  <div class="area-card" style="left:792px">
    <div class="area-photo" role="img" aria-label="Car interior being sprayed with disinfectant" style="background:linear-gradient(135deg,#3a3f47,#1e2126 55%,#6b1a22)"></div>
    <h3>Transportation</h3>
    <p>Sed ut perspiciatis unde omnis iste natus error sit</p>
  </div>
</section>

<section class="contact">
  <h2 class="section-title" style="top:3083px">CONTACT FORM</h2>
  <p class="section-lead" style="top:3158px">Sed ut perspiciatis unde omnis iste natus error sit voluptatem accusantium doloremque laudantium.Sed ut perspiciatis unde omnis iste natus error sit voluptatem accusantium doloremque laudant</p>
  <div class="field" style="left:195px;top:3237px;width:392px">Name</div>
  <div class="field" style="left:611px;top:3237px;width:392px">Email</div>
  <div class="field" style="left:195px;top:3309px;width:392px">Phone</div>
  <div class="field" style="left:611px;top:3309px;width:392px">Subject</div>
  <div class="field message" style="left:195px;top:3379px;width:808px">Message</div>
  <div class="btn" style="left:423px;top:3499px;width:352px;height:41px;line-height:41px">Submit Now</div>
</section>

<footer class="site-footer">
  <div class="footer-col"><h4 style="left:161px">Get in Touch</h4></div>
  <div class="contact-row" style="top:154px">
    <svg width="30" height="24" viewBox="0 0 30 24" fill="none" stroke="#bbb" stroke-width="1.4"><rect x="1" y="3" width="28" height="19"/><path d="M1 3l14 11L29 3"/></svg>
    <span>info@mail.com<br>info@treldmist.com</span>
  </div>
  <div class="contact-row" style="top:222px">
    <svg width="30" height="32" viewBox="0 0 30 32" fill="none" stroke="#bbb" stroke-width="1.4"><rect x="8" y="1" width="16" height="30" rx="2"/><path d="M8 25h16M8 6h16"/></svg>
    <span>+123 456 7890<br>+123 456 7890</span>
  </div>
  <div class="contact-row" style="top:294px">
    <svg width="30" height="32" viewBox="0 0 30 32" fill="none" stroke="#bbb" stroke-width="1.4"><path d="M15 26S6 16 6 10a9 9 0 0 1 18 0c0 6-9 16-9 16z"/><circle cx="15" cy="10" r="3"/><path d="M4 24l-3 7h28l-3-7"/></svg>
    <span>123, Main Road, New<br>City, My Country 123456</span>
  </div>

  <div class="footer-col"><h4 style="left:432px">Quick Links</h4></div>
  <ul class="footer-list" style="left:437px;top:147px">
    <li>About us</li><li>Blog</li><li>Contact us</li><li>Faq</li><li>Insurance</li><li>Contact us</li>
  </ul>

  <div class="footer-col"><h4 style="left:641px">Our Services</h4></div>
  <ul class="footer-list" style="left:637px;top:147px">
    <li>Residential</li><li>Commercial</li><li>Transportation</li><li>Gyms</li><li>Educational &amp; Daycare</li><li>Real Estate</li>
  </ul>

  <div class="footer-brand">TRELDMIST</div>
  <span class="social" style="left:953px" aria-label="Social profile link"></span>
  <span class="social" style="left:990px" aria-label="Second social profile link"></span>

  <div class="footer-bar"><p>©2020 Treld Mist. All rights reserved</p></div>
</footer>

</body>
</html>
```